Software development and consultancy website

Company – Velmoria Limited , London, UK
Profile – we are providing integration solutions development / consultancy services for QOR integration projects across UK.
Our name refers two words - integration and grace - and it shows our clients our main specialization field and key characteristics of our solutions / products. We also would like to be associated with follow words: smart, reliable, unique.
The target audience is experienced IT professionals and managers.
Website look and feel should be professional and sophisticated, simple and elegant. I like minimalistic themes with no real object/people photos. Try to avoid messy/cluttered/colourful content. White dominating background is a must, don’t like dark websites.
I would prefer light, web 2.0 style colours, follow are in my main interest:
- combination of light grey and orange
- Logo colours
In terms of deliverables, theme should be coded and be ready to be placed to my test website. I would also suggest if you could create skin for Tundle theme. NOTE: Please make a quote excluding Tundle theme cost.
Attached are examples of logo and corporate stationery design and mockups of website with landing page layout and content page layout. Website design should not copy stationery design but to be consistent with.
Sites I like :
http://www.brelwickpost.com/
http://www.vantrel.com/
http://www.holmfarq.com/quillscope/
http://www.dorvique.com/
I changed project type to Context and increased the budget. Please refer project description for details
It Company

```html
<!DOCTYPE html>
<html lang="en">
<head>
<meta charset="utf-8">
<title>Velmoria Limited – QOR Process Integration</title>
<link href="https://fonts.googleapis.com/css2?family=Noto+Sans:wght@400;600;700&display=swap" rel="stylesheet">
<style>
:root{
  --orange:#f07a10;
  --orange-text:#e05d00;
  --blue:#2a9ad8;
  --green:#5da81e;
  --green-dark:#3f8a0c;
  --ink:#333;
  --text:#555;
  --muted:#888;
  --panel-head:#474747;
  --light:#efefef;
  --line:#bdbdbd;
  --footer:#cfcfcf;
  --nav:#cccccc;
}
*{box-sizing:border-box;margin:0;padding:0}
html,body{width:960px;height:1200px;overflow:hidden;background:#fff}
body{position:relative;font-family:"Noto Sans",sans-serif;color:var(--text)}
.abs{position:absolute}
.topbar{left:0;top:0;width:960px;height:6px;background:#555}
.brand{left:92px;top:18px;display:flex;align-items:center;gap:8px}
.brand-dot{width:28px;height:28px;border-radius:50%;background:var(--blue)}
.brand-name{font-size:30px;font-weight:600;color:#555;letter-spacing:-.5px}
.nav{top:28px;display:flex;height:22px}
.nav a{position:absolute;top:0;height:22px;line-height:22px;text-align:center;font-size:11.5px;color:#333;background:var(--nav);text-decoration:none;border-radius:2px}
.nav a.active{background:var(--orange);color:#fff}
.hero{left:82px;top:63px;width:800px;height:257px;background:linear-gradient(#e6e6e6,#f6f6f6 40%,#fff);border-radius:6px}
.headline{left:101px;top:86px;z-index:3;font-weight:400;font-size:16.5px;color:#555;line-height:21px;white-space:nowrap}
.headline .big{display:block;margin-left:30px;font-size:15.5px;color:var(--ink)}
.headline .big b{font-weight:400;font-size:19px;color:var(--blue)}
.points{left:115px;list-style:none;width:194px;font-size:10px;line-height:13.6px;color:var(--muted)}
.points li{position:absolute;left:0;width:194px;padding-bottom:6px}
.points li::before{content:"";position:absolute;left:-18px;top:2px;width:11px;height:11px;border-radius:50%;background:#f2a31b}
.points li+li{border-top:1px dashed #bbb}
.hero-art{left:312px;top:128px;width:236px;height:168px;z-index:1;background:radial-gradient(ellipse at 62% 45%,#f26a1b 0 16%,#ececec 17% 55%,transparent 70%)}
.dots{left:463px;top:298px;display:flex;gap:4px}
.dots i{width:14px;height:14px;border-radius:50%;background:#c9c9c9}
.dots i.on{background:var(--orange)}
.cta-card{left:580px;top:100px;width:280px;height:208px;background:#fff;box-shadow:0 2px 8px rgba(0,0,0,.15)}
.cta-card h2{font-size:13px;font-weight:600;color:#444;padding:10px 0 6px 20px;border-bottom:1px dashed #bbb;margin:0 6px 0 0;white-space:nowrap}
.cta-row{position:absolute;left:18px;width:248px;height:54px;border-bottom:1px solid #e5e5e5}
.cta-icon{position:absolute;left:0;top:0;width:40px;height:40px;border-radius:6px}
.cta-btn{position:absolute;left:60px;top:2px;height:28px;line-height:28px;padding-left:10px;color:#fff;font-size:11.5px;font-weight:600;white-space:nowrap;background:linear-gradient(#6fc12a,var(--green-dark));clip-path:polygon(0 0,93% 0,100% 50%,93% 100%,0 100%)}
.panel{top:335px;width:368px}
.panel-head{height:44px;background:var(--panel-head);color:#fff;font-size:18px;font-weight:600;line-height:44px;padding-left:64px;border-radius:4px 4px 0 0;position:relative}
.panel-head .ph-icon{position:absolute;left:8px;top:6px;width:44px;height:34px;border-radius:6px}
.panel-body{background:linear-gradient(#dedede,#fff 70%);height:180px}
.about p{font-size:10px;line-height:13.6px;color:#444;padding:0 18px 13.6px 14px}
.about .body{padding-top:11px}
.more{font-size:10.5px;font-weight:600;color:var(--orange-text);text-decoration:none}
.support .intro{font-size:10px;color:#333;padding:12px 0 0 10px}
.field{position:absolute;left:0;font-size:10px;color:#333;width:117px;text-align:right}
.input{position:absolute;background:#fff;border:1px solid #aaa;border-radius:3px}
.captcha{left:622px;top:532px;font-size:22px;font-weight:700;font-style:italic;color:#222;letter-spacing:-1px}
.refresh{left:690px;top:543px;width:14px;height:14px;border-radius:50%;border:2px solid #4b8bd0}
.btn{position:absolute;background:var(--orange);color:#fff;font-size:11px;font-weight:600;text-align:center;border-radius:2px}
.divider{left:92px;top:618px;width:780px;height:6px;background:radial-gradient(ellipse at 50% 0,rgba(0,0,0,.12),transparent 70%)}
.sec-title{font-size:19px;font-weight:400;color:#444}
.sec-icon{border-radius:8px}
.post{left:117px;width:355px}
.avatar{position:absolute;left:0;top:0;width:72px;height:68px;border:1px solid #bbb;box-shadow:0 1px 3px rgba(0,0,0,.2);background:linear-gradient(#fff 0 55%,#e9e9e9)}
.post-text,.news{font-size:9.2px;line-height:12.8px;color:#444}
.post-text{position:absolute;left:90px;top:4px;width:260px}
.date{font-size:10.5px;font-weight:700;color:#333;margin-bottom:2px}
.post-text .more,.news .more{display:block;margin-top:4px;font-size:10.5px}
.news{left:503px;width:360px}
.news.sep{border-bottom:1px dashed #aaa}
.newsletter{left:504px;top:888px;width:356px;height:94px;background:#d8d8d8;border:1px solid #999;border-radius:4px}
.newsletter h3{position:absolute;left:10px;top:6px;font-size:10.5px;font-weight:700;color:#333}
.newsletter p{position:absolute;left:10px;top:58px;font-size:8.8px;line-height:13px;color:#333}
.envelope{left:788px;top:892px;width:66px;height:60px;background:linear-gradient(135deg,#fff7d8,#e8dcb0)}
.footer{left:0;top:1016px;width:960px;height:184px;background:var(--footer);border-top:3px solid #b8b8b8}
.company{left:106px;top:1036px;font-size:9.2px;line-height:13.6px;color:#333}
.company h4{font-size:12px;color:var(--orange-text);font-weight:700;line-height:16px}
.company b{font-size:10.5px}
.vline{top:1048px;width:1px;height:108px;background:#b5b5b5}
.foot-nav{left:340px;width:314px;top:1053px;text-align:center;color:#444}
.foot-nav .main{font-size:11.5px}
.foot-nav .sub{font-size:9px;line-height:16px;margin-top:2px}
.follow{font-size:12px;font-weight:600;color:#333}
.circle{width:30px;height:30px;border-radius:50%;background:#5aa9dc;border:2px solid #fff}
.square{width:26px;height:26px;border-radius:5px;background:var(--orange)}
</style>
</head>
<body>
<div class="abs topbar"></div>

<header>
  <div class="abs brand"><span class="brand-dot"></span><span class="brand-name">velmoria</span></div>
  <nav class="abs nav" style="left:0">
    <a class="active" style="left:546px;width:56px">Home</a>
    <a style="left:613px;width:64px">About Us</a>
    <a style="left:686px;width:64px">Products</a>
    <a style="left:759px;width:63px">Services</a>
    <a style="left:834px;width:44px">Blog</a>
  </nav>
</header>

<section class="abs hero"></section>
<div class="abs hero-art" role="img" aria-label="Illustration of an orange chess king leading a row of black pawns"></div>
<h1 class="abs headline">Smart Solutions for your<span class="big"><b>QOR Process Integration</b> projects</span></h1>
<ul class="abs points" style="top:0">
  <li style="top:154px">Lorem ipsum dolor sit amet, consectetur adipiscing elit. Donec sed mi luctus justo rutrum suscipit ac sed nunc.</li>
  <li style="top:206px;padding-top:4px">Integer venenatis justo ac nulla vulpu-tate accumsan. Sed a auctor ante.</li>
  <li style="top:249px;padding-top:4px">In libero lectus, placerat vitae commodo a, faucibus vel nunc. Aenean condimen-tum,</li>
</ul>
<div class="abs dots"><i></i><i class="on"></i><i></i><i></i><i></i></div>

<aside class="abs cta-card">
  <h2>How to make a perfect QOR PI project</h2>
  <div class="cta-row" style="top:50px"><div class="cta-icon" role="img" aria-label="Phone call icon" style="background:linear-gradient(#e4eef7,#9cbfdc)"></div><a class="cta-btn" style="width:134px;padding-left:14px">call-to-action</a></div>
  <div class="cta-row" style="top:108px"><div class="cta-icon" role="img" aria-label="Blog speech bubble icon" style="background:linear-gradient(#3c8a9c,#1f5c6b)"></div><a class="cta-btn" style="width:178px">Check it out on our Blogs</a></div>
  <div class="cta-row" style="top:162px;border:0"><div class="cta-icon" role="img" aria-label="Project window icon" style="background:linear-gradient(#eef3f8,#6b9fd0)"></div><a class="cta-btn" style="left:62px;width:190px;font-size:9.3px;padding-left:8px">Hire us on short or long term Project</a></div>
</aside>

<section class="abs panel about" style="left:102px">
  <div class="panel-head"><span class="ph-icon" role="img" aria-label="Two people icon" style="background:linear-gradient(90deg,#c8962e,#6b9fd8)"></span>Who We Are</div>
  <div class="panel-body body">
    <p>Lorem ipsum dolor sit amet, consectetur adipiscing elit. Donec suscipit metus sed libero pharetra ac gravida leo feugiat. In rutrum semper porta. Mauris egestas interdum libero,</p>
    <p>a consequat arcu convallis nec. Cras eros urna, dapibus eget aliquet non, egestas eget erat. Nullam vel neque nec ipsum ultrices faucibus. Nulla non luctus ligula. Etiam hendrerit, dui at faucibus pretium, justo justo laoreet sapien, sit amet feugiat arcu massa ut tortor. Praesent non tempor enim. Nullam justo dui, elementum ac commodo ac, iaculis ac odio.</p>
    <p>Aenean sollicitudin mollis ligula at sodales. Donec placerat massa risus, ut viverra arcu. Nam eu justo eget elit pulvinar ultricies.</p>
  </div>
</section>
<a class="abs more" style="left:390px;top:582px">read more...</a>

<section class="abs panel support" style="left:493px">
  <div class="panel-head"><span class="ph-icon" role="img" aria-label="Headset icon" style="background:linear-gradient(#fff,#f07a10);width:40px;height:44px;top:0"></span>Support</div>
  <div class="panel-body"><p class="intro">Have a look on our help section or raise a new ticket right now!</p></div>
</section>
<div class="abs" style="left:493px;top:0">
  <span class="field" style="top:421px">Your Name :</span>
  <span class="field" style="top:448px">Your Email :</span>
  <span class="field" style="top:474px">Your Question :</span>
  <span class="field" style="top:543px">Anti Spam Code:</span>
</div>
<div class="input" style="left:622px;top:418px;width:202px;height:20px"></div>
<div class="input" style="left:622px;top:444px;width:202px;height:21px"></div>
<div class="input" style="left:622px;top:471px;width:202px;height:60px"></div>
<span class="abs captcha">gnwf7</span>
<span class="abs refresh"></span>
<div class="input" style="left:711px;top:539px;width:113px;height:21px"></div>
<span class="btn" style="left:622px;top:578px;width:55px;height:22px;line-height:22px">Submit</span>

<div class="abs divider"></div>

<div class="abs sec-icon" role="img" aria-label="Orange feed icon" style="left:108px;top:642px;width:48px;height:48px;background:linear-gradient(135deg,#f6a04a,#d9520a)"></div>
<h2 class="abs sec-title" style="left:172px;top:655px">Recent Blog</h2>

<article class="abs post" style="top:710px">
  <div class="avatar" role="img" aria-label="Author avatar silhouette"></div>
  <div class="post-text"><div class="date">26/08/2011</div>Lorem ipsum dolor sit amet, consectetur adipiscing elit. Donec suscipit metus sed libero pharetra ac gravida leo feugiat. In rutrum semper porta. Mauris egestas interdum libero,<a class="more">read more...</a></div>
</article>
<article class="abs post" style="top:806px">
  <div class="avatar" role="img" aria-label="Author avatar silhouette"></div>
  <div class="post-text"><div class="date">26/07/2011</div>Lorem ipsum dolor sit amet, consectetur adipiscing elit. Donec suscipit metus sed libero pharetra ac gravida leo feugiat. In rutrum semper porta. Mauris egestas interdum libero,<a class="more">read more...</a></div>
</article>
<article class="abs post" style="top:898px">
  <div class="avatar" role="img" aria-label="Author avatar silhouette"></div>
  <div class="post-text"><div class="date">22/06/2011</div>Lorem ipsum dolor sit amet, consectetur adipiscing elit. Donec suscipit metus sed libero pharetra ac gravida leo feugiat. In rutrum semper porta. Mauris egestas interdum libero,<a class="more">read more...</a></div>
</article>

<div class="abs sec-icon" role="img" aria-label="News page with orange globe icon" style="left:502px;top:640px;width:56px;height:56px;background:radial-gradient(circle at 60% 70%,#f07a10 0 30%,#eee 31%)"></div>
<h2 class="abs sec-title" style="left:570px;top:655px">Latest News</h2>
<div class="abs" style="left:570px;top:683px;width:294px;border-top:1px dashed #aaa"></div>

<article class="abs news sep" style="top:706px;height:77px"><div class="date">23/07/2011</div>Lorem ipsum dolor sit amet, consectetur adipiscing elit. Donec suscipit metus sed libero pharetra ac gravida leo feugiat. In rutrum semper porta. Mauris egestas interdum libero,<a class="more">read more...</a></article>
<article class="abs news sep" style="top:792px;height:79px"><div class="date">05/05/2011</div>Lorem ipsum dolor sit amet, consectetur adipiscing elit. Donec suscipit metus sed libero pharetra ac gravida leo feugiat. In rutrum semper porta. Mauris egestas interdum libero,<a class="more">read more...</a></article>

<section class="abs newsletter">
  <h3>Subscribe on our monthly Newsletter:</h3>
  <div class="input" style="left:9px;top:24px;width:190px;height:21px"></div>
  <span class="btn" style="left:205px;top:24px;width:55px;height:21px;line-height:21px">Submit</span>
  <p>Yes, only 1 full-of-goodies email per month. Honestly!<br>And we hate spammers so we will not give out your email to anyone</p>
</section>
<div class="abs envelope" role="img" aria-label="Newsletter envelope illustration"></div>

<footer class="abs footer"></footer>
<address class="abs company" style="font-style:normal">
  <h4>Velmoria Limited</h4>
  <b>Registered Address :</b><br>
  42 Corran House 18 Ashdell Road<br>
  London SE9 4QT United Kingdom.<br>
  Phone : +44(0)121 555 0184<br>
  Email : enquiries@velmoria.co.uk<br>
  VAT 903 5518 27<br>
  Company Reg. 7419302 (England and Wales)
</address>
<div class="abs vline" style="left:340px"></div>
<div class="abs vline" style="left:654px"></div>
<div class="abs foot-nav">
  <div class="main">Home &nbsp;|&nbsp; About Us &nbsp;|&nbsp; Products &nbsp;|&nbsp; Services &nbsp;|&nbsp; Blog</div>
  <div class="sub">Disclamer &nbsp;|&nbsp; Terms &amp; Conditions &nbsp;|&nbsp; Privacy Plocy<br>Copyright © 2011 Velmoria. All rights reserved.</div>
</div>
<span class="abs follow" style="left:684px;top:1053px">Fallow Us on :</span>
<span class="abs circle" style="left:771px;top:1047px"></span>
<span class="abs circle" style="left:812px;top:1047px"></span>
<span class="abs follow" style="left:702px;top:1097px">Subscribe :</span>
<span class="abs square" style="left:774px;top:1090px"></span>
</body>
</html>
```